TALVEXO needs a Sleek, Professional and Serious Web Design, this web design is aiming to be famous!

Dear Designers,

We need a web design for a new company based on the Internet named "talvexo". I have already worked with PQ to get my logo and it has been a wonderful experience which I want to repeat. We are kind of work social network, the web page will be mostly used to write comments on businesses around the world to help workers find which company fit the best for them. This website is also here to help people finding work by giving them the tools to make the right research.

For contents inspiration, you could see on the added files a sketch of the website but I am not asking you following it because it was just for giving the contents.

We do not have any example regarding website that we do like because all are coming so generic. We would like a very sleek website, where surfing become very intuitive and ergonomic (Glimmerly is not very ergonomic for example from our point of view). The website must reflect professionalism and seriousness and worker, world connexion.

We will be pleased to accept original designs as long as they fit to our requirements and if it is properly made of course: e.g. web page looking like a newspaper etc.

About colours, we are not decided yet but we are aiming a light orange (pastel style) or dark bluish green. Also, it comes to our attention that a web site mostly realized in grey-scale will be very interesting (touch of colour will be accepted as well if it miss too much dynamism) .

We will give the feedback as soon as possible because we would like to have 5 pages but it will be only very small changes on the next ones. (like adding 4 buttons)

Target Market(s)

Our target is relatively large because it is all people of working age, in numbers we can say a range of people aged from 18 to 45 years.

Industry/Entity Type

Internet

Number of Pages Required

3 page

Font styles to use
Sans Serif

Requirements
Must have
• Elements that must be on the web page are exposed below:
• - company logo ( .ai & .eps files on added files)
• - 4 buttons (Searcher "highlighted" / Advises / Jobs / Solutions)
• - login/account window
• - language button (e.g. a flag)
• - Window companies searcher (the most important, refer to the sketch)
• - classic menu down the page - about us / contact us / conditions / site map / community / politics / publicity / languages / copyright etc.
Nice to have
• We want a professional and serious website.
Should not have
• If you have a doubt, just ask us because nothing are coming to our mind.

```html
<!DOCTYPE html>
<html lang="en">
<head>
<meta charset="utf-8">
<title>TALVEXO – Companies Searcher</title>
<link rel="stylesheet" href="https://fonts.googleapis.com/css2?family=Source+Sans+3:wght@300;400;600;700&display=swap">
<style>
:root{
  --header-bg:#fafafa;
  --ink:#2b2b2b;
  --brand-blue:#0a78d1;
  --brand-blue-dark:#0862b0;
  --nav-active:#1a7ec8;
  --hero-top:#0b6fbd;
  --hero-mid:#0d7ccc;
  --hero-edge:#075a9e;
  --panel-bg:#f0f1f3;
  --field-border:#cfd3d7;
  --placeholder:#8a8f95;
  --ad-text:#8c8c8c;
  --footer-bg:#3a3a3a;
  --white:#ffffff;
}
*{margin:0;padding:0;box-sizing:border-box}
html,body{width:1200px;height:783px;overflow:hidden}
body{font-family:"Source Sans 3","Source Sans Pro",sans-serif;color:var(--ink);background:var(--white);position:relative}

.site-header{position:absolute;left:0;top:0;width:1200px;height:88px;background:var(--header-bg)}
.brand{position:absolute;left:67px;top:22px;display:flex;align-items:center;gap:10px;font-size:34px;font-weight:700;color:#333;letter-spacing:.5px;text-decoration:none}
.brand-dot{width:26px;height:26px;border-radius:50%;background:#333}
.main-nav{position:absolute;left:461px;top:37px;display:flex;gap:18px;font-size:14px;font-weight:600;text-transform:uppercase}
.main-nav a{color:var(--ink);text-decoration:none}
.main-nav a.is-active{color:var(--nav-active)}
.language-select{position:absolute;left:836px;top:25px;width:144px;height:42px;border:1px solid #cfcfcf;border-radius:3px;background:var(--white);font-size:13px;padding:0 12px;display:flex;align-items:center;justify-content:space-between;color:#444}
.login-button{position:absolute;left:988px;top:25px;width:145px;height:43px;background:var(--brand-blue);border:1px solid var(--brand-blue-dark);border-radius:3px;color:var(--white);font-size:13px;font-weight:600;display:flex;align-items:center;justify-content:center}

.hero{position:absolute;left:0;top:88px;width:1200px;height:569px;background:radial-gradient(ellipse at 45% 45%,var(--hero-mid) 0%,var(--hero-top) 55%,var(--hero-edge) 100%)}
.hero-map{position:absolute;left:110px;top:50px;width:830px;height:510px;border-radius:40%;background:radial-gradient(ellipse,rgba(255,255,255,.12),rgba(255,255,255,0) 70%)}
.hero-title{position:absolute;left:0;top:120px;width:992px;text-align:center;font-size:50px;font-weight:300;letter-spacing:4.5px;color:var(--white)}
.search-panel{position:absolute;left:302px;top:215px;width:386px;height:233px;background:var(--panel-bg);padding:29px 26px 0 27px;box-shadow:0 14px 16px -10px rgba(0,0,0,.45);border-bottom:3px solid #c9ccd0}
.search-field{display:block;width:333px;height:51px;border:1px solid var(--field-border);background:var(--white);font-size:14px;color:var(--placeholder);padding:0 16px;line-height:49px;margin-bottom:13px;box-shadow:inset 0 1px 2px rgba(0,0,0,.08)}
.search-button{display:flex;width:333px;height:50px;background:var(--brand-blue);border:1px solid var(--brand-blue-dark);color:var(--white);font-size:14px;font-weight:600;align-items:center;justify-content:center;margin-top:-1px}
.ad-slot{position:absolute;left:935px;top:46px;width:198px;height:470px;background:var(--white);display:flex;align-items:center;justify-content:center;text-align:center;font-size:28px;font-weight:300;line-height:27px;color:var(--ad-text)}

.site-footer{position:absolute;left:0;top:657px;width:1200px;height:63px;background:var(--footer-bg);display:flex;justify-content:center;align-items:center;gap:47px;font-size:16px;font-weight:300;text-transform:uppercase}
.site-footer a{color:var(--white);text-decoration:none}
.copyright{position:absolute;left:0;top:744px;width:1200px;text-align:center;font-size:11px;color:#333}
</style>
</head>
<body>
<header class="site-header">
  <a class="brand" href="#"><span class="brand-dot"></span>TALVEXO</a>
  <nav class="main-nav">
    <a class="is-active" href="#">Company</a>
    <a href="#">Advises</a>
    <a href="#">Jobs</a>
    <a href="#">Solutions</a>
    <a href="#">About us</a>
  </nav>
  <div class="language-select">LANGUAGE
    <svg width="10" height="7" viewBox="0 0 10 7"><path d="M1 1l4 4 4-4" fill="none" stroke="#333" stroke-width="2"/></svg>
  </div>
  <div class="login-button">LOGIN ACCOUNT</div>
</header>

<section class="hero">
  <div class="hero-map" role="img" aria-label="Dotted world map in light blue"></div>
  <h1 class="hero-title">COMPANIES SEARCHER</h1>
  <form class="search-panel">
    <span class="search-field">COMPANY NAME / VAT NUMBER</span>
    <span class="search-field">CITY / POST CODE / COUNTRY</span>
    <span class="search-button">SEARCH NOW</span>
  </form>
  <aside class="ad-slot">ADD<br>HERE</aside>
</section>

<footer class="site-footer">
  <a href="#">About us</a>
  <a href="#">Contact us</a>
  <a href="#">Community</a>
  <a href="#">Publicity</a>
  <a href="#">Conditions</a>
  <a href="#">Politics</a>
  <a href="#">Language</a>
</footer>
<p class="copyright">COPYRIGHT © 2015 TALVEXO. ALL RIGHTS RESERVED</p>
</body>
</html>
```